Local Chiropractor Needs Up Scale Webdesign

This website needs to have an upscale look with a very modern feel. Below is the information and websites to reference

Add Logo that is attached

Build a color scheme similar to this website image titled "chiro-1"

Must Include these pages in a horizontal menu bar in this order:
Home, Meet Our Staff, Patient Testimonials, Videos, Work Place Wellness, Contact

Build a "classy looking" Make An Appointment Button into the header with the contact info below

Phone Number:
555-314-2760

Address:
4182 Maple Fern Court, #305
Larkmoor, MN 55492

This website needs 4 rotating banners. Please reference a layout similar to this for the banners: http://drkelrom.com/. However design it nicer than this website, this website is very boring and doesn't flow with the colors properly

Below are the description for each banner

Rotating Banner #1
Use Image: Pediatrics
Two lines of text. First line title line, second description. Use Latin text for fill

Rotating Banner #2
Use Image: Aging Gracefully

Rotating Banner #3
Use Image: Pregnancy

Rotating Banner #4
Use Image: Athletics

I'd like to see a free consultation box similar to the "chiro-1" image. Fields to include are: First Name, Last Name, Phone Number, Comments.

For the body, please fill it with latin text. Please design a professional body layout. You can include a box in the right column for the hours

Office Hours
Monday: 8:00-11:00, 2:00-5:00
Tuesday: 8:30-11:00, 2:00-5:30
Wednesday: 8:00-11:00, 2:00-5:00
Thursday: 10:00-12:00, 2:30-5:00
Friday: 8:00-10:00, 1:00-5:00
Saturday: Closed
Sunday: Closed

For the footer please design something similar to the: http://drkelrom.com/

Also include in the Footer: Powered by Brightpath Site Co

Chiropractor

```html
<!DOCTYPE html>
<html lang="en">
<head>
<meta charset="utf-8">
<title>Evergreen Vale Chiropractic</title>
<link rel="stylesheet" href="https://fonts.googleapis.com/css2?family=Questrial&display=swap">
<style>
:root{
  --dark:#1f1f1f;
  --green:#7eaa1b;
  --green-light:#a5c83a;
  --green-pale:#d9ec7a;
  --orange:#d6952a;
  --text:#3b3b3b;
  --field:#ededed;
  --white:#ffffff;
}
*{box-sizing:border-box;margin:0;padding:0}
html,body{width:935px;height:1200px;overflow:hidden;background:var(--white)}
body{position:relative;font-family:"Questrial",sans-serif;color:var(--text)}
.abs{position:absolute}

/* header */
.site-header{left:0;top:0;width:935px;height:113px;background:var(--dark)}
.brand{left:176px;top:38px;display:flex;align-items:center;gap:10px}
.brand-dot{width:30px;height:30px;border-radius:50%;background:var(--green)}
.brand-name{font-size:21px;color:var(--green-light);line-height:1.05}
.appointment{left:560px;top:30px;width:200px;height:36px}
.appointment-label{left:587px;top:31px;width:147px;height:26px;line-height:26px;text-align:center;color:var(--white);font-size:10.5px;letter-spacing:.3px}
.header-contact{right:176px;top:69px;text-align:right;font-size:8px;line-height:12.5px;color:var(--green-light);white-space:nowrap}
.header-contact span{color:var(--orange)}

/* nav */
.main-nav{left:0;top:113px;width:935px;height:28px;background:var(--green);display:flex;justify-content:center;align-items:center;gap:29px;padding-left:6px}
.main-nav a{color:var(--white);text-decoration:none;font-size:10.5px}

/* hero */
.hero{left:0;top:141px;width:935px;height:379px;background:linear-gradient(160deg,#f1f3f6 0%,#e3e7ec 45%,#d6dbe1 70%,#eef0f3 100%)}
.hero-title{left:176px;top:404px;font-size:21px;color:#222;letter-spacing:.3px;font-weight:400}
.hero-text{left:176px;top:433px;font-size:10px;line-height:13px;color:#333}
.hero-dots{left:698px;top:500px;display:flex;gap:7px}
.hero-dots i{width:11px;height:11px;border-radius:50%;background:var(--green)}
.hero-dots i.active{background:var(--orange)}

/* welcome */
.welcome-title{left:176px;top:558px;font-size:21px;color:var(--green);line-height:23px;font-weight:400}
.welcome-title span{display:block;color:var(--orange);font-size:18px}
.welcome-text{left:177px;top:631px;width:345px;font-size:7.6px;line-height:9.9px}
.services-title{left:176px;top:718px;font-size:21px;color:var(--green);font-weight:400}
.services-text{left:177px;top:744px;width:345px;font-size:7.6px;line-height:9.9px}
.service{top:794px;width:106px}
.service svg{display:block;margin-left:18px}
.service h3{margin-top:8px;font-weight:400;font-size:8px;color:var(--orange);text-align:center}
.service p{margin-top:4px;padding-left:4px;font-size:7.4px;line-height:9.2px}

/* sidebar */
.consult{left:577px;top:554px;width:183px;height:388px;background:var(--dark);border-radius:2px}
.consult-banner{left:585px;top:549px;width:168px;height:50px}
.consult-head{left:585px;top:556px;width:168px;text-align:center;color:var(--white);font-size:14px}
.consult-head small{display:block;font-size:7.5px;color:var(--green-pale);margin-top:1px}
.form-lead{left:587px;top:613px;font-size:10px;color:var(--white)}
.field{left:586px;width:165px;height:19px;background:var(--field);border-radius:2px;font-size:7.6px;color:#555;padding:4px 7px}
.submit{left:586px;top:773px;width:76px;height:22px;background:var(--orange);border-radius:2px;color:var(--white);font-size:8px;text-align:center;line-height:22px}
.hours-title{left:586px;top:816px;font-size:14px;color:var(--white);font-weight:400}
.hours-list{left:586px;top:838px;font-size:7.8px;line-height:11.7px;color:var(--white);list-style:none}

/* footer */
.site-footer{left:0;top:986px;width:935px;height:180px;background:var(--dark)}
.footer-heading{top:1018px;font-size:14px;color:var(--orange);font-weight:400}
.footer-contact{left:175px;top:1047px;list-style:none;color:#ddd;font-size:7.8px}
.footer-contact li{display:flex;gap:8px;align-items:flex-start;margin-bottom:10px;line-height:10px}
.footer-contact svg{flex:none;margin-top:1px}
.map{left:395px;top:1044px;width:145px;height:98px;border:2px solid #555;background:linear-gradient(135deg,#e9e6df,#dcd8cf 60%,#e6e2da)}
.footer-hours{left:613px;top:1040px;font-size:8px;line-height:11.7px;color:var(--white);border-collapse:collapse}
.footer-hours td{padding:0}
.footer-hours td:first-child{width:52px}
.footer-bar{left:0;top:1166px;width:935px;height:30px;background:var(--green)}
.footer-bottom{left:0;top:1196px;width:935px;height:4px;background:var(--dark)}
.copyright{left:176px;top:1177px;font-size:7.8px;color:var(--white)}
.powered{right:183px;top:1176px;font-size:7.8px;color:var(--white)}
</style>
</head>
<body>

<header class="site-header abs"></header>
<div class="brand abs"><span class="brand-dot"></span><span class="brand-name">Evergreen Vale<br>Chiropractic</span></div>
<svg class="appointment abs" viewBox="0 0 200 36" aria-hidden="true">
  <polygon points="4,12 28,12 28,36 4,36 12,24" fill="#b97a1c"/>
  <polygon points="196,12 172,12 172,36 196,36 188,24" fill="#b97a1c"/>
  <rect x="27" y="1" width="146" height="26" fill="#d6952a"/>
</svg>
<div class="appointment-label abs">MAKE AN APPOINTMENT</div>
<div class="header-contact abs">
  <span>Address:</span> 4182 Maple Fern Court, #305 Larkmoor, MN 55492<br>
  <span>Phone Number:</span> 555-314-2760
</div>

<nav class="main-nav abs">
  <a href="#">Home</a><a href="#">Meet Our Staff</a><a href="#">Patient Testimonials</a><a href="#">Videos</a><a href="#">Work Place Wellness</a><a href="#">Contact</a>
</nav>

<section class="hero abs" role="img" aria-label="Banner photo: two skiers descending a snowy slope among snow-covered trees"></section>
<h1 class="hero-title abs">LOROM IPSUM DOLOR SIMET</h1>
<p class="hero-text abs">Ut enim ad minim veniam, quis nostrud exercitation<br>ullamco laboris nisi ut aliquip ex ea commodo consequat.</p>
<div class="hero-dots abs"><i class="active"></i><i></i><i></i><i></i></div>

<h2 class="welcome-title abs">WELCOME TO EVERGREEN VALE<span>CHIROPRACTIC HEALTH CENTER WEBSITE</span></h2>
<p class="welcome-text abs">Lorem ipsum dolor sit amet, consectetur adipiscing elit, sed do eiusmod tempor incididunt ut labore et dolore magna aliqua. Ut enim ad minim veniam, quis nostrud exercitation ullamco laboris nisi ut aliquip ex ea commodo consequat. Duis aute irure dolor in reprehenderit in voluptate velit esse cillum dolore eu fugiat nulla pariatur. Excepteur sint occaecat cupidatat non proident, sunt in culpa qui officia deserunt mollit anim id est laborum.</p>

<h2 class="services-title abs">OUR SERVICES</h2>
<p class="services-text abs">Duis aute irure dolor in reprehenderit in voluptate velit esse cillum dolore eu fugiat nulla pariatur. Excepteur sint occaecat cupidatat non proident, sunt in culpa qui officia.</p>

<div class="service abs" style="left:183px">
  <svg width="72" height="72" viewBox="0 0 72 72" aria-hidden="true"><circle cx="36" cy="36" r="35" fill="none" stroke="#7eaa1b" stroke-width="1"/><path d="M26 46 C24 32 34 24 47 23 C48 36 40 46 26 46 Z" fill="#7eaa1b"/><path d="M27 46 C32 38 38 32 43 28" stroke="#fff" stroke-width="2" fill="none"/></svg>
  <h3>HEALTH &amp; WELLNESS</h3>
  <p>Duis aute irure dolor in reprehenderit in vouptat velit esse cillum dolore eu fugiat nulla pariatur.</p>
</div>
<div class="service abs" style="left:307px">
  <svg width="72" height="72" viewBox="0 0 72 72" aria-hidden="true"><circle cx="36" cy="36" r="35" fill="none" stroke="#7eaa1b" stroke-width="1"/><path d="M36 22 C41 29 40 34 36 36 C32 34 31 29 36 22 Z" fill="#7eaa1b"/><path d="M23 40 H49 V46 C49 48 47 49 45 49 H27 C25 49 23 48 23 46 Z" fill="#7eaa1b"/></svg>
  <h3>THERAPEUTIC TREATMENT</h3>
  <p>Duis aute irure dolor in reprehederit in volutate velit esse cillum dolore eu fugiat nulla pariatur.</p>
</div>
<div class="service abs" style="left:429px">
  <svg width="72" height="72" viewBox="0 0 72 72" aria-hidden="true"><circle cx="36" cy="36" r="35" fill="none" stroke="#7eaa1b" stroke-width="1"/><ellipse cx="36" cy="46" rx="12" ry="4.5" fill="#7eaa1b"/><ellipse cx="36" cy="38.5" rx="10" ry="4" fill="#7eaa1b"/><ellipse cx="35" cy="31.5" rx="7.5" ry="3.5" fill="#7eaa1b"/><ellipse cx="36" cy="25.5" rx="5" ry="3" fill="#7eaa1b"/></svg>
  <h3>MESSAGE THERPAY</h3>
  <p>Duis aute irure dolor in reprehenrit in voluptate velit esse cillum dolore eu fugiat nulla pariatur.</p>
</div>

<aside class="consult abs"></aside>
<svg class="consult-banner abs" viewBox="0 0 168 50" aria-hidden="true">
  <polygon points="0,0 168,0 168,36 84,50 0,36" fill="#7eaa1b"/>
  <rect x="0" y="0" width="168" height="2" fill="#a5c83a"/>
  <polygon points="70,42 98,42 84,47" fill="#a5c83a"/>
</svg>
<div class="consult-head abs">FREE CONSULTATION<small>CONTACT US TODAY!</small></div>
<div class="form-lead abs">Complete Form Below ...</div>
<div class="field abs" style="top:632px">First Name</div>
<div class="field abs" style="top:655px">Last Name</div>
<div class="field abs" style="top:678px">Phone Number</div>
<div class="field abs" style="top:702px;height:60px">Comments</div>
<div class="submit abs">Submit</div>
<h3 class="hours-title abs">Office Hours</h3>
<ul class="hours-list abs">
  <li>Monday: 8:00-11:00, 2:00-5:00</li>
  <li>Tuesday: 8:30-11:00, 2:00-5:30</li>
  <li>Wednesday: 8:00-11:00, 2:00-5:00</li>
  <li>Thursday: 10:00-12:00, 2:30-5:00</li>
  <li>Friday: 8:00-10:00, 1:00-5:00</li>
  <li>Saturday: Closed</li>
  <li>Sunday: Closed</li>
</ul>

<footer class="site-footer abs"></footer>
<h4 class="footer-heading abs" style="left:175px">CONTACT US</h4>
<h4 class="footer-heading abs" style="left:394px">GET DIRECTIONS</h4>
<h4 class="footer-heading abs" style="left:613px">OFFICE HOURS</h4>
<ul class="footer-contact abs">
  <li><svg width="10" height="12" viewBox="0 0 10 12" aria-hidden="true"><path d="M5 0 C2 0 0 2 0 4.6 C0 8 5 12 5 12 C5 12 10 8 10 4.6 C10 2 8 0 5 0 Z" fill="#fff"/><circle cx="5" cy="4.5" r="1.8" fill="#1f1f1f"/></svg><span>4182 Maple Fern Court,<br>#305 Larkmoor, MN 55492</span></li>
  <li><svg width="10" height="10" viewBox="0 0 10 10" aria-hidden="true"><path d="M2 0 L4 2.5 L3 4 C4 5.5 5 6.5 6 7 L7.5 6 L10 8 L8.5 10 C4 9.5 0.5 6 0 1.5 Z" fill="#fff"/></svg><span>555-314-2760</span></li>
  <li><svg width="10" height="8" viewBox="0 0 10 8" aria-hidden="true"><rect x="0" y="0" width="10" height="8" fill="#fff"/><path d="M0 0 L5 4.5 L10 0" stroke="#1f1f1f" fill="none"/></svg><span>info@evergreenvale.com</span></li>
</ul>
<div class="map abs" role="img" aria-label="Street map showing the clinic location"></div>
<table class="footer-hours abs">
  <tr><td>Monday:</td><td>8:00-11:00, 2:00-5:00</td></tr>
  <tr><td>Tuesday:</td><td>8:30-11:00, 2:00-5:30</td></tr>
  <tr><td>Wednesday:</td><td>8:00-11:00, 2:00-5:00</td></tr>
  <tr><td>Thursday:</td><td>10:00-12:00, 2:30-5:00</td></tr>
  <tr><td>Friday:</td><td>8:00-10:00, 1:00-5:00</td></tr>
  <tr><td>Saturday:</td><td>Closed</td></tr>
  <tr><td>Sunday:</td><td>Closed</td></tr>
</table>
<div class="footer-bar abs"></div>
<div class="footer-bottom abs"></div>
<p class="copyright abs">Copyright ©2015 EvergreenVale. All Rights Reserved.</p>
<p class="powered abs">Powered by Brightpath Site Co</p>

</body>
</html>
```